Dental Office Business Card

We need a business card for our pediatric dentistry office.
On one side the design needs to contain the following:
our logo (attached)
Vento Pediatric Grins
Soraya Kadbelani, DDS
Board Certified Pediatric Dentist
Tel: (555) 318-2747)
Fax: (555) 264-8031
Email: info@ventopediatricgrins.example
Web: www.ventopediatricgrins.example
Address: 41 Brindle Ave, Suite 208, Wellesley, MA 02099

On the other side of the card, the design needs to have an appointment reminder (date and time as well as day of the week) similar to the design attached (no need for appointment reason “For”)

```html
<!DOCTYPE html>
<html lang="en">
<head>
<meta charset="utf-8">
<title>Vento Pediatric Grins – Business Card</title>
<link rel="stylesheet" href="https://fonts.googleapis.com/css2?family=Baloo+2:wght@600;700;800&display=swap">
<style>
  :root {
    --mint: #a6d5aa;
    --ink: #1e1b1c;
    --paper: #ffffff;
    --shadow: rgba(40, 80, 45, 0.35);
  }
  * { margin: 0; padding: 0; box-sizing: border-box; }
  html, body { width: 1200px; height: 1200px; overflow: hidden; }
  body {
    background: var(--mint);
    font-family: "Baloo 2", sans-serif;
    color: var(--ink);
    position: relative;
  }
  .card {
    position: absolute;
    left: 171px;
    width: 858px;
    height: 501px;
    background: var(--paper);
    box-shadow: 6px 12px 18px var(--shadow);
  }
  .card--front { top: 75px; }
  .card--back { top: 620px; }

  .holder-name {
    position: absolute; left: 75px; top: 124px;
    font-size: 40px; font-weight: 700; color: var(--mint); line-height: 1; white-space: nowrap;
  }
  .holder-title {
    position: absolute; left: 75px; top: 180px;
    font-size: 20px; font-weight: 700; line-height: 1; white-space: nowrap;
  }
  .contact-list { position: absolute; left: 78px; top: 266px; list-style: none; }
  .contact-list li {
    display: flex; align-items: center; height: 37.5px;
    font-size: 19px; font-weight: 700; white-space: nowrap;
  }
  .contact-list svg { width: 17px; height: 17px; margin-right: 20px; flex: none; }
  .contact-list .web { color: var(--mint); }

  .brand {
    position: absolute; left: 500px; top: 110px; width: 310px; height: 250px;
    display: flex; flex-direction: column; align-items: center; justify-content: center; gap: 18px;
  }
  .brand-dot { width: 120px; height: 120px; border-radius: 50%; background: var(--mint); }
  .brand-name { font-size: 28px; font-weight: 700; color: var(--ink); text-align: center; line-height: 1.1; white-space: nowrap; }

  .appt-heading {
    position: absolute; left: 0; right: 0; top: 64px; text-align: center;
    font-size: 46px; font-weight: 800; letter-spacing: 13px; padding-left: 13px; line-height: 1;
  }
  .field { position: absolute; left: 95px; width: 666px; display: flex; align-items: flex-end; }
  .field-label { width: 162px; font-size: 34px; font-weight: 800; letter-spacing: 9px; line-height: 1; }
  .field-line { flex: 1; border-bottom: 3px solid var(--ink); margin-bottom: 4px; }
  .field--date { top: 222px; }
  .field--time { top: 350px; }
  .weekdays {
    position: absolute; left: 95px; top: 296px; width: 675px;
    display: flex; justify-content: space-between; list-style: none;
    font-size: 25px; font-weight: 700; line-height: 1;
  }
  .weekdays li { display: flex; align-items: center; }
  .weekdays li::before {
    content: ""; width: 22px; height: 22px; border: 2.5px solid var(--ink); margin-right: 7px;
  }
</style>
</head>
<body>
  <section class="card card--front">
    <h1 class="holder-name">Soraya Kadbelani, DDS</h1>
    <p class="holder-title">Board Certified Pediatric Dentist</p>
    <ul class="contact-list">
      <li><svg viewBox="0 0 24 24"><path fill="#a6d5aa" d="M6.6 10.8a15 15 0 0 0 6.6 6.6l2.2-2.2a1 1 0 0 1 1-.25 11.4 11.4 0 0 0 3.6.57 1 1 0 0 1 1 1V20a1 1 0 0 1-1 1A17 17 0 0 1 3 4a1 1 0 0 1 1-1h3.5a1 1 0 0 1 1 1c0 1.250.2 2.450.57 3.57a1 1 0 0 1-.25 1z"/></svg>(555) 318-2747</li>
      <li><svg viewBox="0 0 24 24"><path fill="#a6d5aa" d="M6 2h12v5H6zM3 8h18a1 1 0 0 1 1 1v8h-4v5H6v-5H2V9a1 1 0 0 1 1-1zm5 7v5h8v-5z"/></svg>(555) 264-8031</li>
      <li><svg viewBox="0 0 24 24"><path fill="#a6d5aa" d="M3 5h18v14H3zm2 2v.5l7 4.5 7-4.5V7z"/></svg>info@ventopediatricgrins.example</li>
      <li class="web"><svg viewBox="0 0 24 24"><circle cx="12" cy="12" r="9" fill="none" stroke="#1e1b1c" stroke-width="2.2"/><path d="M3 12h18M12 3c3 3 3 15 0 18M12 3c-3 3-3 15 0 18" fill="none" stroke="#1e1b1c" stroke-width="1.8"/></svg>www.ventopediatricgrins.example</li>
      <li><svg viewBox="0 0 24 24"><path fill="#a6d5aa" d="M12 2a7 7 0 0 1 7 7c0 5-7 13-7 13S5 14 5 9a7 7 0 0 1 7-7zm0 4.5a2.5 2.5 0 1 0 0 5 2.5 2.5 0 0 0 0-5z"/></svg>41 Brindle Ave, Suite 208, Wellesley, MA 02099</li>
    </ul>
    <div class="brand">
      <span class="brand-dot"></span>
      <span class="brand-name">Vento Pediatric Grins</span>
    </div>
  </section>

  <section class="card card--back">
    <h2 class="appt-heading">APPOINTMENT</h2>
    <div class="field field--date"><span class="field-label">DATE</span><span class="field-line"></span></div>
    <ul class="weekdays">
      <li>Mon</li><li>Tue</li><li>Wed</li><li>Thu</li><li>Fri</li><li>Sat</li><li>Sun</li>
    </ul>
    <div class="field field--time"><span class="field-label">TIME</span><span class="field-line"></span></div>
  </section>
</body>
</html>
```